External Shop Front Signage Design

We need design ideas for outdoor signage to go on our shopfront, windows and glass doors at our new location for Kestrel Physio. We want to use our existing logo and colour schemes but want it to be dark/black background to match our new gym facility & so that the colours & writing stand out from the street. We would like it to be a minimalist, modern design but also be clear that we are a physiotherapy practice with a gym facility. We have tried some designs but have found them to be too busy, and too many words. We would like something more classy, clear, and simple. I have attached photos of the current street views & some of the designs we have had put together that we didn't like. Our logo is attached as well and our website for reference is www.kestrelclinic.com.au

Industry/Entity Type

Physiotherapy / Health

Font styles to use
Other font styles liked:
• Lufga Bold or Poppins Bold/Itallic

Colors
00AB8E
00BBA5
67D7C9
C6EFE9
E9F9F6
59FF00
82FF00
B8FF75
E3FFCB
F4FFEA

Requirements
Must have
• Obvious logo that pops when driving past
Nice to have
• Something that makes it clear we are mainly physiotherapy with gym facility
Should not have
• Too many words

```html
<!DOCTYPE html>
<html lang="en">
<head>
<meta charset="utf-8">
<title>Kestrel Physio – Shopfront Signage</title>
<link href="https://fonts.googleapis.com/css2?family=Poppins:ital,wght@0,500;0,600;0,700;1,700;1,800&display=swap" rel="stylesheet">
<style>
:root{
  --sign:#2b2a2a;
  --pane-edge:#1f3a33;
  --frame:#b98c6e;
  --lime:#82FF00;
  --mint:#3fe3c2;
  --white:#ffffff;
  --label:#d9262a;
  --page:#eeeeec;
  --accent:linear-gradient(90deg,var(--lime),var(--mint));
}
*{box-sizing:border-box;margin:0;padding:0}
html,body{width:1200px;height:898px;overflow:hidden;background:var(--page)}
body{position:relative;font-family:"Poppins",sans-serif;color:var(--white)}
.view-label{position:absolute;font-weight:600;color:var(--label);letter-spacing:.5px;line-height:1.05}
.sign{position:absolute;background:var(--sign)}
.accent-bar{position:absolute;left:0;right:0;height:4px;background:var(--accent)}
.brand{display:flex;align-items:center;gap:.18em;font-weight:600;color:var(--white);line-height:1;white-space:nowrap}
.brand-mark{width:.32em;height:.32em;background:var(--lime)}
.center{position:absolute;display:flex;align-items:center;justify-content:center}
.frame{position:absolute;background:var(--frame)}
.pane{position:absolute;background:var(--sign);border:2px solid var(--pane-edge)}
.pane::after{content:"";position:absolute;left:0;right:0;bottom:0;height:3px;background:var(--accent)}
.tagline{font-weight:800;font-style:italic;background:var(--accent);-webkit-background-clip:text;background-clip:text;color:transparent;white-space:nowrap}
.services{list-style:none;font-weight:700;text-transform:uppercase}
.entrance{font-weight:600;text-transform:uppercase;line-height:1.2}
.chevrons{color:var(--lime);font-weight:800;letter-spacing:-2px}
.merge{position:absolute;background:var(--sign)}
</style>
</head>
<body>

<!-- Street left -->
<div class="view-label" style="left:207px;top:2px;font-size:20px">STREET LEFT</div>
<div class="sign" style="left:76px;top:52px;width:462px;height:85px">
  <div class="center" style="inset:0 0 4px 0"><span class="brand" style="font-size:40px"><span class="brand-mark"></span>Kestrel</span></div>
  <div class="accent-bar" style="bottom:0"></div>
</div>
<div class="frame" style="left:161px;top:172px;width:294px;height:175px">
  <div class="sign center" style="left:10px;top:8px;width:276px;height:34px"><span class="tagline" style="font-size:11px">GET BETTER. GET MOVING. GET STRONG.</span></div>
  <div class="pane" style="left:11px;top:48px;width:114px;height:118px">
    <ul class="services" style="font-size:7px;line-height:16.5px;padding:6px 0 0 7px">
      <li>Physiotherapy</li><li>Remedial Massage</li><li>Podiatry</li><li>Hydrotherapy</li><li>Athletic Development</li><li>Strength&amp;Conditioning</li>
    </ul>
  </div>
  <div class="pane" style="left:129px;top:48px;width:75px;height:118px"></div>
  <div class="pane" style="left:207px;top:48px;width:79px;height:118px"></div>
  <div class="center" style="left:129px;top:48px;width:157px;height:110px"><span class="brand" style="font-size:34px"><span class="brand-mark"></span>Kestrel</span></div>
</div>

<!-- Street right -->
<div class="view-label" style="left:834px;top:12px;font-size:20px">STREET RIGHT</div>
<div class="sign" style="left:617px;top:74px;width:558px;height:103px">
  <div class="center" style="inset:0 0 4px 0"><span class="brand" style="font-size:40px"><span class="brand-mark"></span>Kestrel</span></div>
  <div class="accent-bar" style="bottom:0"></div>
</div>
<div class="frame" style="left:732px;top:227px;width:309px;height:185px">
  <div class="sign center" style="left:10px;top:7px;width:290px;height:38px"><span class="tagline" style="font-size:12px">GET BETTER. GET MOVING. GET STRONG.</span></div>
  <div class="pane" style="left:11px;top:52px;width:82px;height:121px">
    <ul class="services" style="font-size:4.6px;line-height:11px;padding:22px 0 0 7px">
      <li>Physiotherapy</li><li>Remedial Massage</li><li>Podiatry</li><li>Hydrotherapy</li><li>Athletic Development</li><li>Strength&amp;Conditioning</li>
    </ul>
  </div>
  <div class="pane" style="left:97px;top:52px;width:78px;height:121px"></div>
  <div class="pane" style="left:180px;top:52px;width:120px;height:121px">
    <div class="entrance" style="position:absolute;left:9px;bottom:10px;font-size:6px">Entrance &amp; Parking<br>at rear of building</div>
    <span class="chevrons" style="position:absolute;right:10px;bottom:9px;font-size:13px">&gt;&gt;&gt;</span>
  </div>
  <div class="center" style="left:97px;top:56px;width:180px;height:90px"><span class="brand" style="font-size:38px"><span class="brand-mark"></span>Kestrel</span></div>
</div>

<!-- Driveway -->
<div class="view-label" style="left:209px;top:480px;font-size:20px">DRIVEWAY</div>
<div class="sign" style="left:113px;top:527px;width:393px;height:106px">
  <div class="center" style="left:0;right:0;top:14px;height:60px"><span class="brand" style="font-size:44px"><span class="brand-mark"></span>Kestrel</span></div>
  <div class="entrance" style="position:absolute;right:36px;top:85px;font-size:7.5px;font-style:italic;font-weight:700">Entrance &amp; Parking at rear of building</div>
  <span class="chevrons" style="position:absolute;right:10px;top:80px;font-size:14px">&gt;&gt;&gt;</span>
  <div class="accent-bar" style="bottom:0;height:5px"></div>
</div>
<div class="merge" style="left:122px;top:633px;width:384px;height:122px;background:var(--pane-edge)">
  <div class="pane" style="left:3px;top:4px;width:190px;height:115px">
    <ul class="services" style="font-size:11.5px;line-height:15.3px;padding:9px 0 0 10px">
      <li>Physiotherapy</li><li>Remedial Massage</li><li>Podiatry</li><li>Hydrotherapy</li><li>Athletic Development</li><li>Strength&amp;Conditioning</li>
    </ul>
  </div>
  <div class="pane" style="left:198px;top:4px;width:183px;height:115px">
    <div class="tagline" style="position:absolute;right:16px;top:22px;font-size:17.5px;line-height:22px;text-align:right">GET BETTER.<br>GET MOVING.<br>GET STRONG.</div>
  </div>
</div>

<!-- Rear entrance -->
<div class="view-label" style="left:752px;top:462px;font-size:11px">MAIN ENTRANCE<br>REAR OF BUILDING</div>
<div class="sign" style="left:747px;top:522px;width:317px;height:147px">
  <div class="accent-bar" style="top:0;height:5px"></div>
  <div class="center" style="inset:5px 0 0 0"><span class="brand" style="font-size:42px"><span class="brand-mark"></span>Kestrel</span></div>
</div>
<div class="merge" style="left:749px;top:673px;width:310px;height:127px;background:#1a1a1a">
  <div class="pane" style="left:2px;top:0;width:49px;height:125px"></div>
  <div class="pane" style="left:53px;top:0;width:47px;height:125px"></div>
  <div class="pane" style="left:102px;top:0;width:50px;height:125px"></div>
  <div class="pane" style="left:154px;top:0;width:49px;height:125px"></div>
  <div class="pane" style="left:205px;top:0;width:50px;height:125px"></div>
  <div class="pane" style="left:257px;top:0;width:51px;height:125px"></div>
  <div class="center" style="left:4px;top:48px;width:94px;height:28px"><span class="brand" style="font-size:21px"><span class="brand-mark"></span>Kestrel</span></div>
  <div class="center entrance" style="left:102px;top:48px;width:50px;height:28px;font-size:7px">Welcome</div>
  <div class="center" style="left:154px;top:48px;width:49px;height:28px;gap:3px"><span class="entrance" style="font-size:7px">Slide</span><span class="chevrons" style="font-size:9px">&gt;&gt;&gt;</span></div>
  <div class="tagline" style="position:absolute;left:234px;top:40px;font-size:8px;line-height:10.5px">GET BETTER.<br>GET MOVING.<br>GET STRONG.</div>
</div>

</body>
</html>
```